Design a Pizza Themed Self Mailer

I need a self mailer flyer/brochure designed inside and out with a pizza theme. It needs to be legal size (8.5"x14") and be folded so that there are three sections. I have attached a template for you to use. If you need the template in another format them please let me know. I need unique designs created by you and not taken from layoutharbor or other template sites. winner will receive future work for more projects like this. Also, I will purchase works that may not win the contest, but are still good. Contest will be upgraded to guaranteed once I see the quality of work that I am looking for. I may also increase the prize.

I don't need a menu. A menu can be a part of the design, but this is for a trifold mailer. You can have coupons as part of the design or whatever else you think works from a visual standpoint. I am looking for clean designs. Nothing stolen from the internet. I need inside and outside designs.

There will be additional work as I will need TONS of these in the near future. Also, technically it doesn't even have to be pizza. It could be for a grocery store, any kind of restaurant, a dentists office, plumber, car wash, etc. Just anything that could be a local business. I just happened to choose a pizza them because I figured it would be easier.

Example of what I am looking for can be seen here.
http://morvatenstudio.example/qxbseason.html
https://www.portfolane.example/gallery/48190362/Tri-fold-Self-Mailer-for-Hearing-Aid-Company
https://quellonadvertising.example/wp-content/uploads/2017/04/vertical-offset-tri-fold.jpg
https://www.portfolane.example/gallery/48190714/Giant-Pizza-Folded-Menu

```html
<!DOCTYPE html>
<html lang="en">
<head>
<meta charset="utf-8">
<title>Emberly Pizza – Trifold Self Mailer</title>
<link rel="stylesheet" href="https://fonts.googleapis.com/css2?family=Oswald:wght@400;600;700&family=Roboto+Condensed:wght@400;700&family=Lobster&family=Roboto:wght@400&display=swap">
<style>
:root{
  --page:#ffffff;
  --label:#444444;
  --ink:#161616;
  --panel:#1d1d1d;
  --wood:#2a2a2a;
  --red:#e31e24;
  --green:#3dae2b;
  --lime:#5bc236;
  --white:#ffffff;
  --paper:#f1f1f1;
  --muted:#bdbdbd;
  --orange:#e07b22;
  --gold:#f2c318;
}
*{box-sizing:border-box;margin:0;padding:0}
html,body{width:1200px;height:1048px;overflow:hidden;background:var(--page)}
body{position:relative;font-family:"Roboto Condensed",Arial,sans-serif;color:var(--white)}
.side-label{position:absolute;top:94px;font-family:"Roboto",Arial,sans-serif;font-size:15px;color:var(--label);width:486px;text-align:center}
.mailer{position:absolute;top:133px;width:486px;height:792px;background:var(--panel);overflow:hidden;box-shadow:0 2px 6px rgba(0,0,0,.25)}
.mailer--outside{left:91px}
.mailer--inside{left:625px;background:radial-gradient(ellipse at 50% 40%,#262626,#141414)}
.abs{position:absolute}

/* outside – hero */
.hero{left:0;top:0;width:486px;height:267px;background:linear-gradient(180deg,#333 0%,#1f1f1f 100%)}
.hero-greens{left:0;top:40px;width:60px;height:200px;background:radial-gradient(ellipse at 20% 50%,#4f8a2a 0%,#2e5a1a 45%,transparent 75%)}
.hero-pizza{left:330px;top:115px;width:150px;height:150px;border-radius:50%;background:radial-gradient(circle,#c8502a 0%,#b4401f 45%,#d99a4c 70%,#8a5a2b 100%)}
.hero-tomatoes{left:300px;top:10px;width:180px;height:90px;background:radial-gradient(circle at 70% 40%,#d63a22 0,#d63a22 10%,transparent 11%),radial-gradient(circle at 40% 15%,#e8d33a 0,#e8d33a 7%,transparent 8%),radial-gradient(circle at 88% 85%,#3f7d22 0,#3f7d22 10%,transparent 11%)}
.brand{left:90px;top:22px;width:230px;text-align:center}
.brand-mark{display:inline-block;width:40px;height:40px;border-radius:50%;background:var(--white);border:4px solid var(--green)}
.brand-name{display:block;font-family:"Oswald",sans-serif;font-weight:700;font-size:50px;line-height:1;color:var(--red);letter-spacing:1px;margin-top:4px}
.brand-tagline{font-family:"Oswald",sans-serif;font-size:17px;color:var(--white);margin-top:10px;letter-spacing:.5px}
.brand-hours{display:inline-block;margin-top:8px;background:var(--white);color:var(--ink);font-size:10px;font-weight:700;padding:2px 10px;letter-spacing:.5px}
.order-bar{left:0;top:243px;width:312px;height:24px;background:var(--lime);color:var(--white);font-family:"Oswald",sans-serif;font-weight:600;font-size:15px;line-height:24px;padding-left:52px;letter-spacing:.5px}

/* outside – mailing */
.mail-band{left:0;top:267px;width:486px;height:263px;background:#232323}
.address-area{left:4px;top:271px;width:223px;height:134px;background:var(--paper);color:var(--ink);text-align:center;padding-top:22px}
.address-area h2{font-family:"Roboto Condensed",sans-serif;font-weight:700;font-size:20px;letter-spacing:.5px}
.address-area p{font-size:15px;line-height:1.25;margin-top:4px}
.indicia-area{left:4px;top:460px;width:68px;height:70px;background:var(--paper);color:var(--ink);padding:14px 5px 0}
.indicia-area h3{font-size:7px;font-weight:700}
.indicia-area p{font-size:4.5px;margin-top:6px;line-height:1.3}
.order-now{left:227px;top:271px;width:259px;height:66px;background:var(--red);text-align:center}
.order-now small{display:block;font-family:"Oswald",sans-serif;font-size:12px;letter-spacing:3px;margin-top:6px}
.order-now small::before,.order-now small::after{content:"";display:inline-block;width:34px;border-top:1px solid var(--white);vertical-align:middle;margin:0 6px}
.order-now strong{display:block;font-family:"Oswald",sans-serif;font-weight:400;font-size:30px;line-height:1.1}
.contact-list{left:236px;top:346px;width:240px;font-size:10px;line-height:1.3}
.contact-list li{list-style:none;display:flex;gap:6px;align-items:flex-start;margin-bottom:8px}
.contact-list .web{font-size:14px;font-weight:700;letter-spacing:.5px;align-items:center}
.contact-list svg{flex:none;margin-top:1px}
.slice-photo{left:236px;top:420px;width:250px;height:110px;background:linear-gradient(120deg,#d6913d 0%,#c4441f 40%,#e0b34f 70%,#8c5a2b 100%);border-radius:40px 0 0 0}

/* shared – menu grid */
.menu{left:0;top:537px;width:486px;display:grid;grid-template-columns:repeat(4,1fr);row-gap:6px}
.menu-item{height:112px;text-align:center;position:relative}
.menu-item h4{font-family:"Roboto Condensed",sans-serif;font-weight:700;font-size:12px;color:var(--white)}
.menu-photo{display:block;width:50px;height:50px;margin:5px auto 0;border-radius:50%;background:radial-gradient(circle,#c65a2a 0%,#d89a4a 55%,#a0692f 80%,#6d4420 100%)}
.menu-price{position:absolute;left:10px;top:48px;font-family:"Oswald",sans-serif;font-size:12px;color:var(--orange)}
.menu-price sup{font-size:7px}
.menu-item .toppings{font-size:6px;color:var(--orange);margin-top:4px}
.menu-item .desc{font-size:5.5px;color:var(--muted);line-height:1.3;padding:0 10px;margin-top:1px}

/* shared – footer */
.footer{left:0;top:762px;width:486px;height:30px}
.footer-text{left:0;top:770px;width:486px;height:22px;display:flex;justify-content:center;align-items:center;gap:26px;font-size:10px;font-weight:700;color:var(--white)}
.footer-text span{display:flex;align-items:center;gap:5px}

/* inside – header */
.free-delivery{left:17px;top:23px;width:60px;height:60px;border-radius:50%;background:var(--red);font-family:"Oswald",sans-serif;font-weight:600;font-size:13px;line-height:1.15;text-align:center;padding-top:14px;transform:rotate(-12deg)}
.headline{left:205px;top:10px;width:272px;text-align:center}
.headline .script{font-family:"Lobster",cursive;font-size:30px;line-height:1;color:var(--white)}
.headline .boxed{margin:0 auto;width:259px;height:38px;border:2px solid var(--green);font-family:"Oswald",sans-serif;font-weight:700;font-size:24px;line-height:34px;color:var(--red);background:var(--white);letter-spacing:.5px;text-align:left;padding-left:12px}
.smiley{left:424px;top:47px;width:24px;height:24px;border-radius:50%;background:var(--gold)}
.headline .sub{font-size:10px;font-weight:700;margin-top:4px;letter-spacing:.3px}
.deal{left:20px;top:108px;width:220px;text-align:center;font-family:"Oswald",sans-serif;font-weight:600;line-height:1.15}
.deal .price{font-size:34px;color:var(--lime);font-weight:700}
.deal .price sup{font-size:17px}
.deal .big{font-size:19px}
.deal .mid{font-size:15px}
.deal .pickup{font-size:15px;color:var(--lime)}
.deal .call{font-size:15px;color:var(--red)}
.deal-photo{left:230px;top:95px;width:255px;height:165px;border-radius:50%;background:radial-gradient(ellipse,#c4321e 0%,#d2452a 50%,#e3a94e 72%,#c27a36 86%,transparent 88%)}

/* inside – coupons */
.coupon{background:var(--white);color:var(--ink);border:2px dashed var(--red);outline:3px solid var(--white);text-align:center;display:flex;flex-direction:column}
.coupon p{font-size:8px;font-weight:700;line-height:1.2;padding:6px 4px 0}
.coupon .fine{font-size:6px;font-weight:400;padding-top:3px}
.coupon .amount{font-family:"Oswald",sans-serif;font-weight:600;font-size:25px;margin-top:auto;line-height:1}
.coupon .amount sup{font-size:12px}
.coupon .code{margin:3px 4px 4px;background:var(--green);color:var(--white);font-size:9px;font-weight:700;padding:1px 0}
.coupon .code--red{background:var(--red)}
.coupon--tall .amount{font-size:31px;margin-top:14px}
.coupon--tall .code{margin-top:auto}
.coupons-disclaimer{left:20px;top:507px;width:446px;text-align:center;font-size:6.5px;line-height:1.35;color:var(--white)}
.ribbon{left:48px;top:472px}
.ribbon-text{left:48px;top:472px;width:390px;height:22px;line-height:22px;text-align:center;font-size:9.5px;font-weight:700;color:var(--white);letter-spacing:.3px}
</style>
</head>
<body>

<div class="side-label" style="left:91px">Out Side Mailer</div>
<div class="side-label" style="left:625px">In Side Mailer</div>

<!-- OUTSIDE -->
<section class="mailer mailer--outside">
  <div class="abs hero" role="img" aria-label="Dark wooden table scattered with flour, herbs, chillies and spices"></div>
  <div class="abs hero-greens" role="img" aria-label="Fresh parsley and basil leaves"></div>
  <div class="abs hero-tomatoes" role="img" aria-label="Cherry tomatoes, lemon and herbs"></div>
  <div class="abs hero-pizza" role="img" aria-label="Whole pizza on a wooden serving board"></div>

  <div class="abs brand">
    <span class="brand-mark"></span>
    <span class="brand-name">EMBERLY</span>
    <div class="brand-tagline">· Crispy · Crusty · Spicy</div>
    <div class="brand-hours">HAPPY HOUR : 10 AM TO 8 PM</div>
  </div>
  <div class="abs order-bar">ORDER TODAY AT 956.555.0142</div>

  <div class="abs mail-band"></div>
  <div class="abs address-area">
    <h2>ADDRESS AREA</h2>
    <p>WHITE BACKGROUND<br>OR 10% COLOR TINT</p>
  </div>
  <div class="abs indicia-area">
    <h3>INDICIA AREA</h3>
    <p>WHITE BACKGROUND<br>OR 10% COLOR TINT</p>
  </div>
  <div class="abs order-now">
    <small>ORDER NOW</small>
    <strong>825-555-0177</strong>
  </div>
  <ul class="abs contact-list">
    <li>
      <svg width="10" height="12" viewBox="0 0 10 12"><path d="M5 0a4 4 0 0 0-4 4c0 3 4 8 4 8s4-5 4-8a4 4 0 0 0-4-4zm0 5.6A1.6 1.6 0 1 1 5 2.4a1.6 1.6 0 0 1 0 3.2z" fill="#fff"/></svg>
      14-16 LARKMERE AVENUE, ASHBOURNE VALE,<br>AV4 2QT, UK
    </li>
    <li class="web">
      <svg width="11" height="8" viewBox="0 0 11 8"><rect width="11" height="8" fill="#fff"/><path d="M0 0l5.5 4.5L11 0" fill="none" stroke="#232323" stroke-width="1.2"/></svg>
      WWW.EMBERLYPIZZA.EXAMPLE
    </li>
  </ul>
  <div class="abs slice-photo" role="img" aria-label="Pizza slice being lifted with stretching melted cheese"></div>

  <div class="abs menu">
    <div class="menu-item"><h4>Meat Lover</h4><span class="menu-photo" role="img" aria-label="Meat lover pizza"></span><span class="menu-price"><sup>$</sup>10</span><div class="toppings">Smoked Beef · Parmesan · Basil</div><div class="desc">Hand-stretched dough, slow tomato sauce, fresh mozzarella and oven-roasted toppings.</div></div>
    <div class="menu-item"><h4>Fruit Lover</h4><span class="menu-photo" role="img" aria-label="Fruit lover pizza"></span><span class="menu-price"><sup>$</sup>10</span><div class="toppings">Smoked Beef · Parmesan · Basil</div><div class="desc">Hand-stretched dough, slow tomato sauce, fresh mozzarella and oven-roasted toppings.</div></div>
    <div class="menu-item"><h4>Meat Lover</h4><span class="menu-photo" role="img" aria-label="Meat lover pizza"></span><span class="menu-price"><sup>$</sup>10</span><div class="toppings">Smoked Beef · Parmesan · Basil</div><div class="desc">Hand-stretched dough, slow tomato sauce, fresh mozzarella and oven-roasted toppings.</div></div>
    <div class="menu-item"><h4>Fruit Lover</h4><span class="menu-photo" role="img" aria-label="Fruit lover pizza"></span><span class="menu-price"><sup>$</sup>10</span><div class="toppings">Smoked Beef · Parmesan · Basil</div><div class="desc">Hand-stretched dough, slow tomato sauce, fresh mozzarella and oven-roasted toppings.</div></div>
    <div class="menu-item"><h4>Meat Lover</h4><span class="menu-photo" role="img" aria-label="Meat lover pizza"></span><span class="menu-price"><sup>$</sup>10</span><div class="toppings">Smoked Beef · Parmesan · Basil</div><div class="desc">Hand-stretched dough, slow tomato sauce, fresh mozzarella and oven-roasted toppings.</div></div>
    <div class="menu-item"><h4>Fruit Lover</h4><span class="menu-photo" role="img" aria-label="Fruit lover pizza"></span><span class="menu-price"><sup>$</sup>10</span><div class="toppings">Smoked Beef · Parmesan · Basil</div><div class="desc">Hand-stretched dough, slow tomato sauce, fresh mozzarella and oven-roasted toppings.</div></div>
    <div class="menu-item"><h4>Meat Lover</h4><span class="menu-photo" role="img" aria-label="Meat lover pizza"></span><span class="menu-price"><sup>$</sup>10</span><div class="toppings">Smoked Beef · Parmesan · Basil</div><div class="desc">Hand-stretched dough, slow tomato sauce, fresh mozzarella and oven-roasted toppings.</div></div>
    <div class="menu-item"><h4>Fruit Lover</h4><span class="menu-photo" role="img" aria-label="Fruit lover pizza"></span><span class="menu-price"><sup>$</sup>10</span><div class="toppings">Smoked Beef · Parmesan · Basil</div><div class="desc">Hand-stretched dough, slow tomato sauce, fresh mozzarella and oven-roasted toppings.</div></div>
  </div>

  <svg class="abs footer" width="486" height="30" viewBox="0 0 486 30">
    <path d="M0 8 L9 0 L18 8 L27 0 L36 8 L45 0 L54 8 L63 0 L72 8 L81 0 L90 8 L99 0 L108 8 L117 0 L126 8 L135 0 L144 8 L153 0 L162 8 L171 0 L180 8 L189 0 L198 8 L207 0 L216 8 L225 0 L234 8 L243 0 L252 8 L261 0 L270 8 L279 0 L288 8 L297 0 L306 8 L315 0 L324 8 L333 0 L342 8 L351 0 L360 8 L369 0 L378 8 L387 0 L396 8 L405 0 L414 8 L423 0 L432 8 L441 0 L450 8 L459 0 L468 8 L477 0 L486 8 V30 H0Z" fill="#5bc236"/>
  </svg>
  <div class="abs footer-text">
    <span><svg width="12" height="9" viewBox="0 0 12 9"><rect x=".5" y=".5" width="11" height="8" fill="none" stroke="#fff"/><path d="M.5.5l5.5 4.5 5.5-4.5" fill="none" stroke="#fff"/></svg>hello@emberlypizza.example</span>
    <span><svg width="8" height="12" viewBox="0 0 8 12"><rect x=".5" y=".5" width="7" height="11" rx="1.2" fill="none" stroke="#fff"/><circle cx="4" cy="9.5" r=".8" fill="#fff"/></svg>941.555.0163</span>
  </div>
</section>

<!-- INSIDE -->
<section class="mailer mailer--inside">
  <div class="abs free-delivery">Free<br>Delivery</div>
  <div class="abs headline">
    <div class="script">Meet Your</div>
    <div class="boxed">DELICIOUS PIZZA</div>
    <div class="sub">YOUR RECIPE-YOUR INGRDIENTS-YOUR PIZZA</div>
  </div>
  <div class="abs smiley" role="img" aria-label="Small yellow emoji sticker"></div>

  <div class="abs deal-photo" role="img" aria-label="Large pepperoni pizza with green peppers"></div>
  <div class="abs deal">
    <div class="price"><sup>$</sup>14.<sup>95</sup></div>
    <div class="big">ONE LARGE PIE</div>
    <div class="big">• ONE TOPPING •</div>
    <div class="mid">ONE 2 LITER SODA</div>
    <div class="pickup">PICK UP ONLY</div>
    <div class="call">Call : 973-555-0119</div>
  </div>

  <div class="abs coupon coupon--tall" style="left:11px;top:277px;width:112px;height:179px">
    <p>Add One Appetizer To Any Order</p>
    <p class="fine">Choose from single Order od wings, Potato Skins, or Bruschetta. &amp; ONE Large Pepperoni Pizza</p>
    <div class="amount"><sup>$</sup>15<sup>95</sup></div>
    <div class="code code--red">COUPON 102</div>
  </div>
  <div class="abs coupon" style="left:132px;top:277px;width:97px;height:84px">
    <p>Large Pepperoni Pizza</p>
    <div class="amount"><sup>$</sup>15<sup>95</sup></div>
    <div class="code">COUPON 102</div>
  </div>
  <div class="abs coupon" style="left:249px;top:277px;width:103px;height:84px">
    <p>Small (12") 2-Topping Pizza, Lunch Sized Salad &amp; Two Sodas</p>
    <div class="amount"><sup>$</sup>19<sup>95</sup></div>
    <div class="code">COUPON 101</div>
  </div>
  <div class="abs coupon" style="left:365px;top:277px;width:104px;height:84px">
    <p>Add One Appetizer To Any Order</p>
    <p class="fine">Choose from Single Order of Wings, Potato Skins, or Bruschetta</p>
    <div class="amount"><sup>$</sup>4</div>
    <div class="code">COUPON 104</div>
  </div>
  <div class="abs coupon" style="left:132px;top:375px;width:97px;height:81px">
    <p>Two Medium (14") 1-Topping Pizzas</p>
    <div class="amount"><sup>$</sup>23<sup>95</sup></div>
    <div class="code">COUPON 103</div>
  </div>
  <div class="abs coupon" style="left:249px;top:375px;width:103px;height:81px">
    <p>Large Pepperoni Pizza</p>
    <div class="amount"><sup>$</sup>15<sup>95</sup></div>
    <div class="code">COUPON 102</div>
  </div>
  <div class="abs coupon" style="left:365px;top:375px;width:104px;height:81px">
    <p>Small (12") 2-Topping Pizza, Lunch Sized Salad &amp; Two Sodas</p>
    <div class="amount"><sup>$</sup>19<sup>95</sup></div>
    <div class="code">COUPON 101</div>
  </div>

  <svg class="abs ribbon" width="390" height="22" viewBox="0 0 390 22">
    <path d="M0 0 H390 L380 11 L390 22 H0 L10 11Z" fill="#b3161b"/>
    <path d="M14 0 H376 V22 H14Z" fill="#e31e24"/>
  </svg>
  <div class="abs ribbon-text">WE ARE OFFERING PERSONAL DELIVERY MONDAY- THURSDAY 5PM-9PM</div>
  <p class="abs coupons-disclaimer">Must present coupon when ordering. Not valid with any other offer. No substitutions. One coupon per<br>order. Coupon must be surrendered.</p>

  <div class="abs menu">
    <div class="menu-item"><h4>Meat Lover</h4><span class="menu-photo" role="img" aria-label="Meat lover pizza"></span><span class="menu-price"><sup>$</sup>10</span><div class="toppings">Smoked Beef · Parmesan · Basil</div><div class="desc">Hand-stretched dough, slow tomato sauce, fresh mozzarella and oven-roasted toppings.</div></div>
    <div class="menu-item"><h4>Fruit Lover</h4><span class="menu-photo" role="img" aria-label="Fruit lover pizza"></span><span class="menu-price"><sup>$</sup>10</span><div class="toppings">Smoked Beef · Parmesan · Basil</div><div class="desc">Hand-stretched dough, slow tomato sauce, fresh mozzarella and oven-roasted toppings.</div></div>
    <div class="menu-item"><h4>Meat Lover</h4><span class="menu-photo" role="img" aria-label="Meat lover pizza"></span><span class="menu-price"><sup>$</sup>10</span><div class="toppings">Smoked Beef · Parmesan · Basil</div><div class="desc">Hand-stretched dough, slow tomato sauce, fresh mozzarella and oven-roasted toppings.</div></div>
    <div class="menu-item"><h4>Fruit Lover</h4><span class="menu-photo" role="img" aria-label="Fruit lover pizza"></span><span class="menu-price"><sup>$</sup>10</span><div class="toppings">Smoked Beef · Parmesan · Basil</div><div class="desc">Hand-stretched dough, slow tomato sauce, fresh mozzarella and oven-roasted toppings.</div></div>
    <div class="menu-item"><h4>Meat Lover</h4><span class="menu-photo" role="img" aria-label="Meat lover pizza"></span><span class="menu-price"><sup>$</sup>10</span><div class="toppings">Smoked Beef · Parmesan · Basil</div><div class="desc">Hand-stretched dough, slow tomato sauce, fresh mozzarella and oven-roasted toppings.</div></div>
    <div class="menu-item"><h4>Fruit Lover</h4><span class="menu-photo" role="img" aria-label="Fruit lover pizza"></span><span class="menu-price"><sup>$</sup>10</span><div class="toppings">Smoked Beef · Parmesan · Basil</div><div class="desc">Hand-stretched dough, slow tomato sauce, fresh mozzarella and oven-roasted toppings.</div></div>
    <div class="menu-item"><h4>Meat Lover</h4><span class="menu-photo" role="img" aria-label="Meat lover pizza"></span><span class="menu-price"><sup>$</sup>10</span><div class="toppings">Smoked Beef · Parmesan · Basil</div><div class="desc">Hand-stretched dough, slow tomato sauce, fresh mozzarella and oven-roasted toppings.</div></div>
    <div class="menu-item"><h4>Fruit Lover</h4><span class="menu-photo" role="img" aria-label="Fruit lover pizza"></span><span class="menu-price"><sup>$</sup>10</span><div class="toppings">Smoked Beef · Parmesan · Basil</div><div class="desc">Hand-stretched dough, slow tomato sauce, fresh mozzarella and oven-roasted toppings.</div></div>
  </div>

  <svg class="abs footer" width="486" height="30" viewBox="0 0 486 30">
    <path d="M0 8 L9 0 L18 8 L27 0 L36 8 L45 0 L54 8 L63 0 L72 8 L81 0 L90 8 L99 0 L108 8 L117 0 L126 8 L135 0 L144 8 L153 0 L162 8 L171 0 L180 8 L189 0 L198 8 L207 0 L216 8 L225 0 L234 8 L243 0 L252 8 L261 0 L270 8 L279 0 L288 8 L297 0 L306 8 L315 0 L324 8 L333 0 L342 8 L351 0 L360 8 L369 0 L378 8 L387 0 L396 8 L405 0 L414 8 L423 0 L432 8 L441 0 L450 8 L459 0 L468 8 L477 0 L486 8 V30 H0Z" fill="#5bc236"/>
  </svg>
  <div class="abs footer-text">
    <span><svg width="12" height="9" viewBox="0 0 12 9"><rect x=".5" y=".5" width="11" height="8" fill="none" stroke="#fff"/><path d="M.5.5l5.5 4.5 5.5-4.5" fill="none" stroke="#fff"/></svg>hello@emberlypizza.example</span>
    <span><svg width="8" height="12" viewBox="0 0 8 12"><rect x=".5" y=".5" width="7" height="11" rx="1.2" fill="none" stroke="#fff"/><circle cx="4" cy="9.5" r=".8" fill="#fff"/></svg>941.555.0163</span>
  </div>
</section>

</body>
</html>
```